Square graphic for social media post

I want to create a 1080 x 1080px all-black image for the quote below that I can share on social media. I want the emphasis to be primarily on the quote, secondarily on the portrait, and third (smallest) on the logo. I want the background on the portrait to be edited so it's transparent and just shows the face of the person on a black background (no brick wall visible).

Graphic color: black
Text color: white
Content: "What we went through is going to make the greatest generation of hoteliers our industry has ever seen." << biggest text
Derek Holloway << smaller text
President, Ridgemont Hotels << smaller text
[image of person - use whichever version looks better to you]
[Add Lodging Ledger logo - whichever looks better to you]

This image needs to be readable when sized down much smaller (400x400?) so want the text and portrait to take up most of the space.

I'd like the output both as PNG and original file (preferably Canva). Thanks!

Target Market(s)

Hotel managers

Industry/Entity Type

Hospitality

Font styles to use
Sans Serif

Colors

Designer to choose colors to be used in the design.

Requirements
Must have
• Needs to focus on the quote and the person quoted (the portrait)

```html
<!DOCTYPE html>
<html lang="en">
<head>
<meta charset="utf-8">
<title>Quote Card – Derek Holloway</title>
<link rel="stylesheet" href="https://fonts.googleapis.com/css2?family=Arimo:wght@400;700&display=swap">
<style>
  :root {
    --bg: #000000;
    --ink: #ffffff;
    --portrait-light: #9a9a9a;
    --portrait-dark: #3c3c3c;
  }
  html, body {
    margin: 0;
    padding: 0;
    width: 1200px;
    height: 1200px;
    overflow: hidden;
    background: var(--bg);
  }
  .quote-card {
    display: block;
    width: 1200px;
    height: 1200px;
    background: var(--bg);
    font-family: "Arimo", Arial, sans-serif;
  }
  .quote-frame {
    fill: none;
    stroke: var(--ink);
    stroke-width: 6;
    stroke-linecap: butt;
  }
  .quote-mark {
    fill: var(--ink);
    font-weight: 700;
    font-size: 250px;
  }
  .quote-line {
    fill: var(--ink);
    font-weight: 400;
  }
  .speaker-name {
    fill: var(--ink);
    font-weight: 700;
    font-size: 34px;
    letter-spacing: 0.5px;
  }
  .speaker-title {
    fill: var(--ink);
    font-weight: 400;
    font-size: 26px;
  }
  .brand-name {
    fill: var(--ink);
    font-weight: 700;
    font-size: 20px;
    letter-spacing: 5px;
  }
</style>
</head>
<body>
<svg class="quote-card" viewBox="0 0 1200 1200" xmlns="http://www.w3.org/2000/svg">
  <defs>
    <radialGradient id="portraitTone" cx="50%" cy="42%" r="60%">
      <stop offset="0%" stop-color="var(--portrait-light)"/>
      <stop offset="100%" stop-color="var(--portrait-dark)"/>
    </radialGradient>
  </defs>

  <!-- Frame around the quote -->
  <path class="quote-frame"
        d="M150 181 H1147 Q1169 181 1169 203 V550"/>
  <path class="quote-frame"
        d="M36 311 V643 Q36 665 58 665 H1020"/>

  <!-- Quote marks -->
  <text class="quote-mark" x="22" y="355">&#8220;</text>
  <text class="quote-mark" x="1088" y="768">&#8221;</text>

  <!-- Quote -->
  <text class="quote-line" x="136" y="318" font-size="89" textLength="933" lengthAdjust="spacingAndGlyphs">What we went through</text>
  <text class="quote-line" x="136" y="422" font-size="89" textLength="933" lengthAdjust="spacingAndGlyphs">is going to make the</text>
  <text class="quote-line" x="136" y="500" font-size="64" textLength="933" lengthAdjust="spacingAndGlyphs">greatest generation of hoteliers</text>
  <text class="quote-line" x="136" y="578" font-size="73" textLength="933" lengthAdjust="spacingAndGlyphs">our industry has ever seen</text>

  <!-- Portrait -->
  <circle cx="600" cy="744" r="142" fill="var(--bg)"/>
  <circle class="speaker-portrait" cx="600" cy="744" r="133" fill="url(#portraitTone)"
          role="img" aria-label="Portrait photo of Derek Holloway on a black background"/>

  <!-- Speaker -->
  <text class="speaker-name" x="600" y="917" text-anchor="middle">DEREK HOLLOWAY</text>
  <text class="speaker-title" x="600" y="952" text-anchor="middle">President, Ridgemont Hotels</text>

  <!-- Publisher -->
  <text class="brand-name" x="600" y="1112" text-anchor="middle">LODGING LEDGER</text>
</svg>
</body>
</html>
```